Plakat-Design Workshop gegen Prüfungsangst
Zielgruppe
Prüfungsangst überwinden mittels Workshops: 'Selbsthypnose erlernen'
Zielgruppe Studenten
Schweißausbrüche, Blackout, und Resignation.
Viele kennen diese unangenehmen Momente, wenn eine Prüfung begonnen hat und die Aufgabenstellungen scheinbar unlösbar sind.
Dann ist Entspannung nahezu unmöglich. Das Stresshormon Cortisol wurde bereits ausgeschüttet. Es beeinträchtigt die Erinnerung an das Gelernte.
Die mentale Vorbereitung sollte schon viel eher ansetzen, wenn es noch nicht zu spät ist. Wenn der Körper noch nicht verkrampft ist.
Selbsthypnose vor Prüfungen ist hier eine tolle Möglichkeit.
Mit Hilfe einer geführten Selbsthypnoseanleitung ist es Dir möglich Dein Unterbewusstsein so zu programmieren, dass diese Übererregungszustände vor Prüfungssituationen deutlich reduziert werden.
Aufgabenstellung
DINA 4 Plakat, 'Prüfungsangst?' mit einem Freifeld, wo man Ort, Datum und Zeit der Veranstaltung 'Selbsthypnose erlernen'
(Selbstsicher in die Prüfung) eindrucken kann.
darunter:
Anmeldung: Tel: 01563 8274015
Dipl. Sportl. Henrik Malow Mentaltraining
weitere Infos auch über Einzelsitzungen: www.malow-trance.de

```html
<!DOCTYPE html>
<html lang="de">
<head>
<meta charset="utf-8">
<title>Prüfungsangst? – Workshop Selbsthypnose</title>
<link rel="stylesheet" href="https://fonts.googleapis.com/css2?family=Hind:wght@400;500;600;700&display=swap">
<style>
  :root {
    --red: #e0302a;
    --ink: #111111;
    --paper: #ffffff;
    --rule: #a9a9a9;
    --badge: #d9dcdd;
    --backdrop: #ffffff;
  }
  html, body {
    margin: 0;
    padding: 0;
    width: 881px;
    height: 1200px;
    overflow: hidden;
    background: var(--backdrop);
    font-family: "Hind", Arial, sans-serif;
  }
  .poster {
    position: absolute;
    left: 51px;
    top: 51px;
    width: 770px;
    height: 1090px;
    background: var(--paper);
    box-shadow: 0 4px 14px rgba(0,0,0,0.35);
    overflow: hidden;
    color: var(--ink);
  }
  .hero-photo {
    position: absolute;
    left: 0; top: 0;
    width: 770px; height: 346px;
    background:
      linear-gradient(90deg, rgba(0,0,0,0) 55%, rgba(150,170,200,0.55) 80%, rgba(130,150,180,0.5) 100%),
      linear-gradient(180deg, #b8692c 0%, #a45a26 45%, #8a4b24 70%, #6a4a3c 100%);
  }
  .accent-rule {
    position: absolute;
    left: 0; top: 352px;
    width: 770px; height: 5px;
    background: var(--red);
  }
  .headline {
    position: absolute;
    left: 25px; top: 376px;
    margin: 0;
    font-size: 106px;
    font-weight: 600;
    line-height: 1;
    letter-spacing: -1px;
    color: var(--red);
    white-space: nowrap;
  }
  .symptoms {
    position: absolute;
    left: 28px; top: 493px;
    margin: 0;
    font-size: 35.5px;
    font-weight: 600;
    line-height: 1;
    white-space: nowrap;
  }
  .intro {
    position: absolute;
    left: 27px; top: 541px;
    width: 740px;
    margin: 0;
    font-size: 26.3px;
    font-weight: 400;
    line-height: 34px;
  }
  .claim {
    position: absolute;
    left: 26px; top: 651px;
    margin: 0;
    font-size: 59.5px;
    font-weight: 600;
    line-height: 1;
    color: var(--red);
    white-space: nowrap;
  }
  .coach-photo {
    position: absolute;
    left: 29px; top: 735px;
    width: 216px; height: 308px;
    background: linear-gradient(160deg, #d4d4d2 0%, #a9aaa8 45%, #b8c4d6 75%, #9fb0c8 100%);
  }
  .badge {
    position: absolute;
    left: 195px; top: 938px;
    width: 132px; height: 132px;
    border-radius: 50%;
    background: var(--badge);
    border: 6px solid var(--paper);
  }
  .event-fields {
    position: absolute;
    left: 355px; top: 728px;
    width: 387px;
  }
  .field {
    display: flex;
    align-items: baseline;
    height: 62px;
    font-size: 40px;
    line-height: 1;
  }
  .field-line {
    flex: 1;
    margin-left: 4px;
    border-bottom: 2px solid var(--rule);
  }
  .registration {
    position: absolute;
    left: 355px; top: 921px;
    margin: 0;
    font-size: 22.4px;
    line-height: 26px;
    white-space: nowrap;
  }
  .registration strong { font-weight: 700; }
  .brand {
    position: absolute;
    right: 28px; top: 938px;
    display: flex;
    align-items: center;
    gap: 6px;
    font-size: 16px;
    font-weight: 700;
    color: var(--ink);
    white-space: nowrap;
  }
  .brand-mark {
    width: 13px; height: 13px;
    background: var(--red);
  }
  .footer-band {
    position: absolute;
    left: 0; top: 1054px;
    width: 770px; height: 36px;
    background: var(--red);
  }
</style>
</head>
<body>
  <main class="poster">
    <div class="hero-photo" role="img" aria-label="Foto: Studierende schreiben eine Prüfung in einer Halle, vorne eine gestresste Studentin mit den Händen am Kopf"></div>
    <div class="accent-rule"></div>

    <h1 class="headline">Prüfungsangst?</h1>
    <h2 class="symptoms">Schweißausbrüche, Blackout &amp; Resignation?</h2>
    <p class="intro">Im Workshop ″Selbsthypnose″ lernst Du Strategien, solche Übererregungszustände vor Prüfungen deutlich zu reduzieren.</p>

    <h2 class="claim">Selbstsicher in die Prüfung!</h2>

    <div class="footer-band"></div>

    <div class="coach-photo" role="img" aria-label="Porträtfoto des Mentaltrainers Henrik Malow vor einer Betonwand"></div>
    <div class="badge" aria-hidden="true"></div>

    <div class="event-fields">
      <div class="field">Ort:<span class="field-line"></span></div>
      <div class="field">Datum:<span class="field-line"></span></div>
      <div class="field">Zeit:<span class="field-line"></span></div>
    </div>

    <p class="registration">
      <strong>Anmeldung:</strong><br>
      Tel: 01563 8274015<br>
      Dipl. Sportl. Henrik Malow Mentaltraining<br>
      weitere Infos auch über Einzelsitzungen:<br>
      <strong>www.malow-trance.de</strong>
    </p>

    <div class="brand"><span class="brand-mark"></span>Malow Trance</div>
  </main>
</body>
</html>
```